FILEVAULT9: Data Rescue from hard drives

Create new web site. Our existing site is at www.filevault9.com.au

The site must show that our main business is recovering data from crashed hard disks. Color theme is blue. Existing logo can be used.

I want to be able to change the images and text later.

Text could be like this:

For when you didn't make a backup...

Some information is like gold to your business. We can recover data from corrupted disks. This includes your documents, Mailbox contacts, financials, contracts, photos or records.

Filevault9 has the recovery tools, software and skills. If you have a damaged disk or files we will make our best effort to recover these for you and put them on a new disk, the Cloud, a DVD or other media.

We strongly suggest that in the event of disk damage the less that you attempt to recover files yourself, the better are our chances of getting your files back. Just turn your computer off and get the disk or the whole computer to us.

Our charges are:

•Standard recovery: $450 including GST
(no recovery= no charge)

•Additional work (if required): by arrangement

•New Media: at cost

Recovery service at no charge for computers damaged in WA Bushfires. (Offer does not include supplying free new equipment)

Please see our "Testimonials" link above for remarks by happy customers. We have been in business for nineteen years and plan on staying that way, keeping you in business.

Small business

Business

Coded - Design and coding required

3 page

• Must suit new Google design rules to be mobile-device-friendly.

```html
<!DOCTYPE html>
<html lang="en">
<head>
<meta charset="utf-8">
<title>FILEVAULT9 – Data Rescue</title>
<link href="https://fonts.googleapis.com/css2?family=Open+Sans:ital,wght@0,300;0,400;0,600;0,700;1,400&display=swap" rel="stylesheet">
<style>
:root{
  --navy:#163e6b;
  --navy-deep:#123a66;
  --brand:#1d3557;
  --blue:#1f88d4;
  --hero-a:#16679a;
  --tick:#8cc63f;
  --text:#666d74;
  --title:#1d4f86;
  --line:#e1e4e8;
  --white:#ffffff;
}
*{margin:0;padding:0;box-sizing:border-box}
html,body{width:890px;height:1200px;overflow:hidden;background:var(--white)}
body{position:relative;font-family:"Open Sans",Arial,sans-serif;color:var(--text)}
.abs{position:absolute}

/* header */
.site-header{position:absolute;left:0;top:0;width:890px;height:58px;background:var(--white)}
.logo{position:absolute;left:74px;top:14px;display:flex;align-items:center;gap:8px}
.logo-mark{width:30px;height:30px;border-radius:50%;background:var(--navy)}
.logo-name{font-weight:700;font-size:19px;color:var(--brand);letter-spacing:.3px}
.main-nav{position:absolute;top:26px;left:0;width:890px;font-size:8.4px;color:#4a5560}
.main-nav span{position:absolute;white-space:nowrap}

/* hero */
.hero{position:absolute;left:0;top:58px;width:890px;height:340px;overflow:hidden;
  background:radial-gradient(ellipse at 45% 15%,#5ab3dc 0%,#2d85b8 45%,var(--hero-a) 100%)}
.hero-title{position:absolute;left:73px;top:72px;font-size:35px;font-weight:300;color:var(--white)}
.features{position:absolute;font-size:10.3px;color:var(--white);list-style:none}
.features li{position:relative;padding-left:20px;height:26.5px}
.features svg{position:absolute;left:0;top:2px}
.btn{position:absolute;background:var(--blue);color:var(--white);font-size:9.5px;
  display:flex;align-items:center;justify-content:center;border-radius:2px}
.hero-visual{position:absolute;left:538px;top:82px;width:286px;height:190px;
  background:radial-gradient(ellipse 50% 50% at 50% 58%,rgba(225,229,233,.55) 0%,rgba(190,200,210,.28) 55%,rgba(160,180,200,0) 100%)}
.slide-arrow{position:absolute;width:16px;height:16px}

/* urgent band */
.urgent{position:absolute;left:0;top:397px;width:890px;height:71px;background:var(--navy-deep);
  clip-path:polygon(0 0,100% 0,100% 84%,0 100%)}
.urgent-text{position:absolute;left:73px;top:14px;width:590px;color:var(--white);font-style:italic;
  font-size:7.7px;font-weight:400;line-height:20px}
.urgent-text strong{font-size:13px;font-weight:400}

/* services */
.service{position:absolute;top:506px;width:226px}
.service-img{width:226px;height:125px}
.section-title{font-size:11.4px;font-weight:400;color:var(--title);padding-bottom:8px;display:inline-block;
  border-bottom:1px solid var(--title);margin-top:15px}
.body-copy{font-size:8.2px;line-height:17.6px;margin-top:12px;width:210px}

/* about */
.about-visual{position:absolute;left:76px;top:798px;width:172px;height:182px;
  background:radial-gradient(ellipse 45% 35% at 50% 42%,rgba(90,165,220,.55) 0%,rgba(220,228,235,.6) 70%,rgba(255,255,255,0) 100%)}
.testimonial-quote{font-style:italic;font-size:8px;line-height:16.5px;margin-top:12px;padding-left:18px;width:185px}
.avatar{position:absolute;left:621px;top:953px;width:38px;height:38px;border-radius:50%;
  background:radial-gradient(circle,#ece8e4 0%,#c9ced3 100%)}

/* clients */
.clients{position:absolute;left:0;top:1029px;width:890px;height:62px;border-top:1px solid var(--line);border-bottom:1px solid var(--line)}
.client{position:absolute;top:22px;display:flex;align-items:center;gap:6px;font-size:11px;font-weight:600;color:var(--navy)}
.client i{display:block;width:14px;height:14px;border-radius:50%;background:var(--navy)}

/* footer */
.footer-nav{position:absolute;top:1121px;left:0;width:890px;font-size:8.2px;color:#4a5560}
.footer-nav span{position:absolute;white-space:nowrap}
.copyright{position:absolute;left:73px;top:1145px;font-size:8.2px;color:#4a5560}
.social{position:absolute;top:1130px;width:20px;height:20px;border-radius:50%}
</style>
</head>
<body>

<header class="site-header">
  <div class="logo"><span class="logo-mark"></span><span class="logo-name">FILEVAULT9</span></div>
  <nav class="main-nav">
    <span style="left:315px">Cloud Services</span>
    <span style="left:405px">Emergency Services</span>
    <span style="left:515px">Computer Repairs</span>
    <span style="left:619px">Testimonials</span>
    <span style="left:703px">Our Clients</span>
    <span style="left:780px">About Us</span>
  </nav>
</header>

<section class="hero">
  <h1 class="hero-title">Safe and Secure</h1>
  <ul class="features" style="left:73px;top:140px">
    <li><svg width="10" height="9" viewBox="0 0 10 9"><path d="M1 5l3 3 5-7" fill="none" stroke="var(--tick)" stroke-width="1.8"/></svg>Work is what you do, not where you do it</li>
    <li><svg width="10" height="9" viewBox="0 0 10 9"><path d="M1 5l3 3 5-7" fill="none" stroke="var(--tick)" stroke-width="1.8"/></svg>Access your files, anywhere, any time</li>
    <li><svg width="10" height="9" viewBox="0 0 10 9"><path d="M1 5l3 3 5-7" fill="none" stroke="var(--tick)" stroke-width="1.8"/></svg>Use the best skills, where ever they are</li>
  </ul>
  <ul class="features" style="left:312px;top:140px">
    <li><svg width="10" height="9" viewBox="0 0 10 9"><path d="M1 5l3 3 5-7" fill="none" stroke="var(--tick)" stroke-width="1.8"/></svg>Activate Nimbic's Cloud services</li>
    <li><svg width="10" height="9" viewBox="0 0 10 9"><path d="M1 5l3 3 5-7" fill="none" stroke="var(--tick)" stroke-width="1.8"/></svg>Nimbic Suite is anywhere you want it to be</li>
    <li><svg width="10" height="9" viewBox="0 0 10 9"><path d="M1 5l3 3 5-7" fill="none" stroke="var(--tick)" stroke-width="1.8"/></svg>Available around the clock</li>
  </ul>
  <a class="btn" style="left:74px;top:231px;width:139px;height:30px">Click here for more info</a>
  <div class="hero-visual" role="img" aria-label="Brushed silver cloud illustration"></div>
  <svg class="slide-arrow" style="left:25px;top:168px" viewBox="0 0 16 16"><circle cx="8" cy="8" r="8" fill="#ffffff" opacity=".18"/><path d="M9.5 4.5L6 8l3.5 3.5" fill="none" stroke="#fff" stroke-opacity=".6" stroke-width="1.5"/></svg>
  <svg class="slide-arrow" style="left:851px;top:168px" viewBox="0 0 16 16"><circle cx="8" cy="8" r="8" fill="#ffffff" opacity=".18"/><path d="M6.5 4.5L10 8l-3.5 3.5" fill="none" stroke="#fff" stroke-opacity=".6" stroke-width="1.5"/></svg>
</section>

<section class="urgent">
  <p class="urgent-text"><strong>Urgent Disk Data Recovery Service</strong> some information is like gold to your business. We can recover data from corrupted disks. This might be your Mailbox contacts, financials, contracts, photos or records.</p>
  <a class="btn" style="left:678px;top:17px;width:138px;height:31px">Emergency Disk Recovery</a>
</section>

<section class="service" style="left:73px">
  <div class="service-img" role="img" aria-label="Open hand beneath a floating cloud" style="background:radial-gradient(ellipse 30% 35% at 60% 30%,#f4f5f6 0%,rgba(244,245,246,0) 100%),linear-gradient(90deg,#c9cbce,#8f9398)"></div>
  <h2 class="section-title">Cloud Services</h2>
  <p class="body-copy">Some information is like gold to your business. We can recover data from corrupted disks. This might be your Mailbox contacts, financials, contracts, photos or records.</p>
</section>
<section class="service" style="left:332px">
  <div class="service-img" role="img" aria-label="Businessman touching a cloud icon among device icons" style="background:radial-gradient(ellipse 35% 45% at 55% 35%,#8a8f92 0%,rgba(138,143,146,0) 100%),linear-gradient(135deg,#4e5558,#1f2528)"></div>
  <h2 class="section-title">Emergency Services</h2>
  <p class="body-copy">Some information is like gold to your business. We can recover data from corrupted disks. This might be your Mailbox contacts, financials, contracts, photos or records.</p>
</section>
<section class="service" style="left:590px">
  <div class="service-img" role="img" aria-label="Person with a laptop sitting on a cloud" style="background:radial-gradient(ellipse 40% 30% at 65% 95%,#e8eef5 0%,rgba(232,238,245,0) 100%),linear-gradient(180deg,#2a5a92,#1d4478)"></div>
  <h2 class="section-title">Computer Repairs</h2>
  <p class="body-copy">Some information is like gold to your business. We can recover data from corrupted disks. This might be your Mailbox contacts, financials, contracts, photos or records.</p>
</section>

<div class="about-visual" role="img" aria-label="Desktop monitor showing a cloud with gears"></div>
<section class="abs" style="left:287px;top:803px;width:290px">
  <h2 class="section-title">About Filevault9</h2>
  <p class="body-copy" style="width:290px">Some information is like gold to your business. We can recover data from corrupted disks. This includes your documents, Mailbox contacts, financials, contracts, photos or records.</p>
  <p class="body-copy" style="width:290px;margin-top:18px">Filevault9 has the recovery tools, software and skills. If you have a damaged disk or files we will make our best effort to recover these for you and put them on a new disk, the Cloud, a DVD or other media.</p>
</section>

<section class="abs" style="left:613px;top:803px;width:205px">
  <h2 class="section-title">Testimonials</h2>
  <svg class="abs" style="left:171px;top:17px" width="16" height="8" viewBox="0 0 16 8"><path d="M4 1L1 4l3 3M12 1l3 3-3 3" fill="none" stroke="#9aa1a8" stroke-width="1.2"/></svg>
  <span class="abs" style="left:2px;top:48px;font-size:18px;color:#c8ccd0;font-style:italic">&ldquo;</span>
  <p class="testimonial-quote">Some information is like gold to your business. We can recover data from corrupted disks. This includes your documents, Mailbox contacts, financials, contracts, photos or records.</p>
  <span class="abs" style="left:192px;top:114px;font-size:18px;color:#c8ccd0;font-style:italic">&rdquo;</span>
</section>
<div class="avatar" role="img" aria-label="Customer portrait"></div>
<p class="abs" style="left:671px;top:956px;font-size:8.2px;line-height:15px"><span style="color:var(--title)">Dean Harlow,</span><br>Keystone Safety Group</p>

<section class="clients">
  <svg class="abs" style="left:46px;top:24px" width="12" height="12" viewBox="0 0 12 12"><circle cx="6" cy="6" r="6" fill="#b9bec4"/><path d="M7 3.5L4.5 6 7 8.5" fill="none" stroke="#fff" stroke-width="1.4"/></svg>
  <svg class="abs" style="left:834px;top:24px" width="12" height="12" viewBox="0 0 12 12"><circle cx="6" cy="6" r="6" fill="#b9bec4"/><path d="M5 3.5L7.5 6 5 8.5" fill="none" stroke="#fff" stroke-width="1.4"/></svg>
  <div class="client" style="left:84px"><i></i>Harbourline Marine</div>
  <div class="client" style="left:224px"><i></i>Westcoast Institute</div>
  <div class="client" style="left:392px"><i></i>Coastal Care Network</div>
  <div class="client" style="left:556px"><i></i>Little Steps</div>
  <div class="client" style="left:688px"><i></i>Ridgeway Computers</div>
</section>

<footer>
  <nav class="footer-nav">
    <span style="left:73px">Home</span>
    <span style="left:126px">Cloud Services</span>
    <span style="left:212px">Emergency Services</span>
    <span style="left:318px">Computer Repairs</span>
    <span style="left:418px">Testimonials</span>
    <span style="left:497px">Our Clients</span>
    <span style="left:570px">About Us</span>
  </nav>
  <p class="copyright">Copyright © 2015. Filevault9. All Rights Reserved.</p>
  <span class="social" style="left:718px;background:#2d5a9a" aria-label="Social link"></span>
  <span class="social" style="left:744px;background:#3a9ad9" aria-label="Social link"></span>
  <span class="social" style="left:769px;background:#333" aria-label="Social link"></span>
  <span class="social" style="left:795px;background:#1b6c93" aria-label="Social link"></span>
</footer>

</body>
</html>
```